Corvane Stationery Design

We need design for our stationary, including:
1) Letterhead
- A4/Letter size in landscape and portrait letterhead
- The letterhead must be in a word file, and the address should be editable using the Felixti or Perpetua Titling TTF
- The output file should be in .docx and in .ai.
2) Business card
- The business card will be printed in white paper and single face only, so there should be nothing on the reverse side.
3) Envelope (sizes A4, Letter, and small document)
Please refer to the picture showing some samples of stationary with designs that would fulfill our wish.
We're including the logo in .AI.
Thanks
Target Market(s)
High end investors
Industry/Entity Type
Landscape
Look and feel

```html
<!DOCTYPE html>
<html lang="en">
<head>
<meta charset="utf-8">
<title>Corvane Capital Partners – Stationery</title>
<link href="https://fonts.googleapis.com/css2?family=PT+Sans:wght@400;700&display=swap" rel="stylesheet">
<style>
  :root {
    --backdrop: #e9eaeb;
    --paper: #f4f4f4;
    --brand-blue: #146aa0;
    --ink: #1d1d1d;
    --logo-grey: #3c3f44;
    --band-dark: #444648;
    --window: #e4e5e6;
    --window-edge: #cfd1d3;
  }
  * { box-sizing: border-box; margin: 0; padding: 0; }
  html, body { width: 1200px; height: 741px; overflow: hidden; }
  body {
    background: var(--backdrop);
    font-family: "PT Sans", sans-serif;
    color: var(--ink);
    position: relative;
  }
  .sheet {
    position: absolute;
    background: var(--paper);
    overflow: hidden;
    box-shadow: 0 1px 3px rgba(0,0,0,.12);
  }
  .wordmark {
    position: absolute;
    color: var(--logo-grey);
    font-weight: 400;
    text-transform: uppercase;
    text-align: center;
    line-height: 1;
  }
  .wordmark .name { display: block; letter-spacing: .06em; }
  .wordmark .tag { display: block; letter-spacing: .28em; }
  .contact-list { position: absolute; list-style: none; }
  .contact-list li { display: flex; align-items: flex-start; gap: 4px; }
  .contact-list svg { flex: none; }
  .footer-band { position: absolute; left: 0; right: 0; bottom: 0; }
  .footer-band .blue { position: absolute; left: 0; bottom: 0; background: var(--brand-blue); }
  .footer-band .dark {
    position: absolute; right: 0; bottom: 0; background: var(--band-dark);
    color: #fff; display: flex; align-items: center; justify-content: center;
    letter-spacing: .08em;
  }

  /* Letterhead */
  .letterhead { left: 111px; top: 49px; width: 459px; height: 649px; }
  .letterhead .wordmark { left: 28px; top: 28px; }
  .letterhead .wordmark .name { font-size: 26px; }
  .letterhead .wordmark .tag { font-size: 9.5px; margin-top: 3px; }
  .letterhead .contact-list { left: 341px; top: 26px; font-size: 7.4px; line-height: 1.2; }
  .letterhead .contact-list li { margin-bottom: 3px; }
  .letterhead .edge-tab { position: absolute; right: 0; top: 20px; width: 5px; height: 67px; background: var(--brand-blue); border-radius: 3px 0 0 3px; }
  .letter { position: absolute; left: 66px; top: 167px; width: 340px; font-size: 8.6px; line-height: 11.3px; }
  .letter p { margin-bottom: 11px; }
  .letter .body { margin-bottom: 0; }
  .letter .closing { margin-top: 36px; }
  .signature { display: block; width: 56px; height: 20px; margin-top: 10px; background: linear-gradient(90deg, rgba(40,40,140,.25), rgba(40,40,140,.1)); border-radius: 6px; }
  .letterhead .footer-band { height: 14px; }
  .letterhead .footer-band .blue { width: 310px; height: 11px; clip-path: polygon(0 0,100% 0,97% 100%,0 100%); }
  .letterhead .footer-band .dark { width: 152px; height: 14px; font-size: 8.5px; clip-path: polygon(6% 0,100% 0,100% 100%,0 100%); }

  /* Envelope back */
  .envelope-back { left: 611px; top: 50px; width: 514px; height: 246px; }
  .envelope-back .flap { position: absolute; left: 0; top: 0; right: 0; height: 87px; background: var(--brand-blue); border-radius: 0 0 8px 8px; }
  .envelope-back .wordmark { left: 0; right: 0; top: 26px; color: #fff; }
  .envelope-back .wordmark .name { font-size: 23px; }
  .envelope-back .wordmark .tag { font-size: 8.5px; margin-top: 3px; }

  /* Envelope front */
  .envelope-front { left: 611px; top: 315px; width: 514px; height: 246px; }
  .envelope-front .wordmark { left: 23px; top: 22px; }
  .envelope-front .wordmark .name { font-size: 23px; }
  .envelope-front .wordmark .tag { font-size: 8.5px; margin-top: 3px; }
  .envelope-front .return-address { position: absolute; left: 23px; top: 84px; font-size: 7.8px; display: flex; gap: 4px; align-items: center; }
  .address-window { position: absolute; left: 23px; top: 99px; width: 158px; height: 48px; background: var(--window); border: 1px solid var(--window-edge); border-radius: 5px; }
  .envelope-front .footer-band { height: 17px; }
  .envelope-front .footer-band .blue { width: 352px; height: 13px; clip-path: polygon(0 0,100% 0,98% 100%,0 100%); }
  .envelope-front .footer-band .dark { width: 166px; height: 17px; font-size: 9px; clip-path: polygon(6% 0,100% 0,100% 100%,0 100%); }

  /* Business cards */
  .business-card { top: 583px; width: 208px; height: 116px; }
  .business-card.first { left: 611px; }
  .business-card.second { left: 843px; }
  .business-card .wordmark { left: 16px; top: 44px; }
  .business-card .wordmark .name { font-size: 15px; }
  .business-card .wordmark .tag { font-size: 5.4px; margin-top: 2px; }
  .business-card .divider { position: absolute; left: 125px; top: 19px; width: 1px; height: 66px; background: #9a9a9a; }
  .business-card .holder { position: absolute; left: 130px; top: 19px; }
  .business-card .holder .person { color: var(--brand-blue); font-weight: 700; font-size: 6.5px; display: block; }
  .business-card .holder .role { font-size: 5px; display: block; }
  .business-card .contact-list { left: 130px; top: 47px; font-size: 4.8px; line-height: 1.2; }
  .business-card .contact-list li { margin-bottom: 2.5px; gap: 3px; }
  .business-card .footer-band { height: 10px; }
  .business-card .footer-band .blue { width: 118px; height: 7px; clip-path: polygon(0 0,100% 0,96% 100%,0 100%); }
  .business-card .footer-band .dark { width: 92px; height: 10px; font-size: 5.5px; clip-path: polygon(7% 0,100% 0,100% 100%,0 100%); }
</style>
</head>
<body>

<!-- Letterhead -->
<section class="sheet letterhead" aria-label="Letterhead">
  <div class="wordmark"><span class="name">Corvane</span><span class="tag">Capital Partners</span></div>
  <ul class="contact-list">
    <li><svg width="8" height="8" viewBox="0 0 10 10"><circle cx="5" cy="5" r="5" fill="#146aa0"/><path d="M5 2.2a1.7 1.7 0 0 1 1.7 1.7C6.7 5.3 5 7.6 5 7.6S3.3 5.3 3.3 3.9A1.7 1.7 0 0 1 5 2.2z" fill="#fff"/></svg><span>14-16 Alder Lane, Northgate<br>VIC 3199 Australia</span></li>
    <li><svg width="8" height="8" viewBox="0 0 10 10"><circle cx="5" cy="5" r="5" fill="#146aa0"/><rect x="3" y="3.5" width="4" height="3" rx="1" fill="#fff"/></svg><span>+61 3 9400 1275</span></li>
    <li><svg width="8" height="8" viewBox="0 0 10 10"><circle cx="5" cy="5" r="5" fill="#146aa0"/><rect x="3" y="3" width="4" height="4" fill="#fff"/></svg><span>+61 3 9400 1275</span></li>
    <li><svg width="8" height="8" viewBox="0 0 10 10"><circle cx="5" cy="5" r="5" fill="#146aa0"/><circle cx="5" cy="5" r="1.8" fill="none" stroke="#fff" stroke-width=".9"/></svg><span>info@corvane.com.au</span></li>
  </ul>
  <div class="edge-tab"></div>

  <article class="letter">
    <p>Your Street Address<br>Your City, State&nbsp; Zip<br>Date</p>
    <p style="margin-top:22px">First and Last Name of the Person to whom you are writing<br>Their Street Address<br>City, ST Zip</p>
    <p style="margin-top:20px">Dear Mr./Ms. Full Name:</p>
    <p class="body">You do not want to indent when you are using this format.&nbsp; This is the best format to use when you are writing a persuasive letter.&nbsp;&nbsp; You want to introduce yourself and the topic you are writing about to the reader.&nbsp; Remember that the first rule of writing is to know your audience.&nbsp; In a persuasive letter, you state your opinion or your feelings about something that is important to you after you have introduced yourself. You must sound as professional and passionate as possible.&nbsp; You do not want to belittle the reader or they will not finish reading your letter.&nbsp; Your letter needs to have the facts, reasons, and examples to support your position. Address issues that your reader may have in their argument.</p>
    <p class="body">In a second paragraph, you must have solutions.&nbsp; Without solutions, you are only complaining. Offer assistance in solving the problem.&nbsp; Remind the reader where they can contact you.</p>
    <p class="closing">Sincerely yours,</p>
    <span class="signature" role="img" aria-label="Handwritten signature"></span>
  </article>

  <div class="footer-band"><div class="blue"></div><div class="dark">www.corvane.com.au</div></div>
</section>

<!-- Envelope, back -->
<section class="sheet envelope-back" aria-label="Envelope back">
  <div class="flap"></div>
  <div class="wordmark"><span class="name">Corvane</span><span class="tag">Capital Partners</span></div>
</section>

<!-- Envelope, front -->
<section class="sheet envelope-front" aria-label="Envelope front">
  <div class="wordmark"><span class="name">Corvane</span><span class="tag">Capital Partners</span></div>
  <div class="return-address"><svg width="9" height="9" viewBox="0 0 10 10"><circle cx="5" cy="5" r="5" fill="#146aa0"/><path d="M5 2.2a1.7 1.7 0 0 1 1.7 1.7C6.7 5.3 5 7.6 5 7.6S3.3 5.3 3.3 3.9A1.7 1.7 0 0 1 5 2.2z" fill="#fff"/></svg><span>14-16 Alder Lane, Northgate VIC 3199 Australia</span></div>
  <div class="address-window"></div>
  <div class="footer-band"><div class="blue"></div><div class="dark">www.corvane.com.au</div></div>
</section>

<!-- Business cards -->
<section class="sheet business-card first" aria-label="Business card">
  <div class="wordmark"><span class="name">Corvane</span><span class="tag">Capital Partners</span></div>
  <div class="divider"></div>
  <div class="holder"><span class="person">Mara Ellison</span><span class="role">Director</span></div>
  <ul class="contact-list">
    <li><svg width="6" height="6" viewBox="0 0 10 10"><circle cx="5" cy="5" r="5" fill="#146aa0"/></svg><span>14-16 Alder Lane, Northgate<br>VIC 3199 Australia</span></li>
    <li><svg width="6" height="6" viewBox="0 0 10 10"><circle cx="5" cy="5" r="5" fill="#146aa0"/></svg><span>+61 3 9400 1275</span></li>
    <li><svg width="6" height="6" viewBox="0 0 10 10"><circle cx="5" cy="5" r="5" fill="#146aa0"/></svg><span>+61 3 9400 1275</span></li>
    <li><svg width="6" height="6" viewBox="0 0 10 10"><circle cx="5" cy="5" r="5" fill="#146aa0"/></svg><span>mara@corvane.com.au</span></li>
  </ul>
  <div class="footer-band"><div class="blue"></div><div class="dark">www.corvane.com.au</div></div>
</section>

<section class="sheet business-card second" aria-label="Business card">
  <div class="wordmark"><span class="name">Corvane</span><span class="tag">Capital Partners</span></div>
  <div class="divider"></div>
  <div class="holder"><span class="person">Mara Ellison</span><span class="role">Director</span></div>
  <ul class="contact-list">
    <li><svg width="6" height="6" viewBox="0 0 10 10"><circle cx="5" cy="5" r="5" fill="#146aa0"/></svg><span>14-16 Alder Lane, Northgate<br>VIC 3199 Australia</span></li>
    <li><svg width="6" height="6" viewBox="0 0 10 10"><circle cx="5" cy="5" r="5" fill="#146aa0"/></svg><span>+61 3 9400 1275</span></li>
    <li><svg width="6" height="6" viewBox="0 0 10 10"><circle cx="5" cy="5" r="5" fill="#146aa0"/></svg><span>+61 3 9400 1275</span></li>
    <li><svg width="6" height="6" viewBox="0 0 10 10"><circle cx="5" cy="5" r="5" fill="#146aa0"/></svg><span>mara@corvane.com.au</span></li>
  </ul>
  <div class="footer-band"><div class="blue"></div><div class="dark">www.corvane.com.au</div></div>
</section>

</body>
</html>
```